Varlen Group Business Card design with current logo

hello all , we have abranded logo which i will attach but we need a card double sided designed . one side is easy as its the logo but the other side we want clean and modern. The info needed will be the same text as the card sample attached. no pictures of us though just clean and professinal pls. Logo can be incorporated on the text side to for recognition. Colors are Black , white , red and grey... ideal card would be matt finish high end stock. or a black card so white text ... Sorry i have uploaded al the files i got when I had the logo designed on here.. Oh forgot want to say pls add in the card details EST 1981 and over 40yrs combined experiance
Updates

Hello everyone , I'm really sorry we haven't been able to make a final decision.. There is at least 3 cards that all have there positives over the other two... We will decide by tonight.

Target Market(s)

20-70 wide range but people with money and a education.

Industry/Entity Type

Real Estate Agent

Contact Information for Business Card

One side the Logo choose from the different color logos, black being the one we like most, other side is the details. Clean professional looking fonts. EST 1981 , over 40yrs experiance. Website email and both names and PH# as per the sample card attached

Font styles to use
Other font styles liked:
• Fonts:Code Bold,Code Light, Lucida Fax.

Colors
1b1b1b
757575
c9c9c9
e8e8e8
ffffff
e9e9e9

Requirements
Must have
• Logo and contact info

```html
<!DOCTYPE html>
<html lang="en">
<head>
<meta charset="utf-8">
<title>Varlen Group Business Card</title>
<link href="https://fonts.googleapis.com/css2?family=Lato:wght@300;400;700&display=swap" rel="stylesheet">
<style>
  :root {
    --backdrop: #e9e9e9;
    --card: #1b1b1b;
    --card-edge: #111111;
    --ink: #ffffff;
    --ink-soft: #e8e8e8;
    --ink-muted: #c9c9c9;
    --ink-dim: #757575;
    --rule: #3a3a3a;
  }
  * { box-sizing: border-box; margin: 0; padding: 0; }
  html, body {
    width: 1200px; height: 844px; overflow: hidden;
    background: var(--backdrop);
    font-family: "Lato", Arial, sans-serif;
  }
  .stage {
    width: 1200px; height: 844px;
    display: flex; align-items: center; justify-content: center; gap: 60px;
  }
  .card {
    width: 510px; height: 292px;
    background: var(--card);
    border: 1px solid var(--card-edge);
    position: relative;
    color: var(--ink);
  }
  /* Details side */
  .card--details { display: flex; }
  .brand-block {
    width: 52%;
    display: flex; align-items: center; justify-content: center; gap: 14px;
  }
  .brand-mark { width: 54px; height: 54px; background: var(--ink); }
  .brand-name {
    font-weight: 400; font-size: 26px; letter-spacing: 2px;
    color: var(--ink); line-height: 1.05; text-transform: uppercase;
  }
  .divider {
    width: 1px; background: var(--rule);
    margin: 40px 0;
  }
  .contact {
    flex: 1; padding: 56px 0 0 26px;
    font-size: 14px; line-height: 1.35; color: var(--ink-soft);
  }
  .contact__name { font-weight: 700; font-size: 19px; color: var(--ink); }
  .contact__role { margin-bottom: 14px; }
  .contact__address { margin-bottom: 14px; }
  /* Logo side */
  .card--logo {
    display: flex; flex-direction: column; align-items: center; justify-content: center;
  }
  .card--logo .brand-block { width: auto; gap: 18px; }
  .card--logo .brand-mark { width: 70px; height: 70px; background: var(--ink-muted); }
  .card--logo .brand-name { font-size: 32px; color: var(--ink-muted); }
  .tagline {
    margin-top: 46px;
    font-size: 13px; letter-spacing: 0.5px; color: var(--ink-dim);
  }
</style>
</head>
<body>
  <main class="stage">
    <section class="card card--details" aria-label="Business card, contact side">
      <div class="brand-block">
        <span class="brand-mark"></span>
        <span class="brand-name">Varlen<br>Group</span>
      </div>
      <div class="divider"></div>
      <div class="contact">
        <p class="contact__name">Daniel Marsh</p>
        <p class="contact__role">Managing Director</p>
        <p class="contact__address">48 Harbour Lane, Suite 2<br>Country Name, 654321.</p>
        <p>T: 044-987 654 321</p>
        <p>E: hello@varlengroup.com</p>
        <p>W: www.varlengroup.com</p>
      </div>
    </section>

    <section class="card card--logo" aria-label="Business card, logo side">
      <div class="brand-block">
        <span class="brand-mark"></span>
        <span class="brand-name">Varlen<br>Group</span>
      </div>
      <p class="tagline">EST 1981 and over 40yrs combined experiance</p>
    </section>
  </main>
</body>
</html>
```